High-End audio shop owner needs a business card

I need a personal Business Card for my Audio shop which exists since 1962. We offer high Quality brands, professional Attention and run our own repair-service-department. I look for a design which will be printed on high Quality paper and shall convey trust to the Client that we are very serious. Language is german.

```html
<!DOCTYPE html>
<html lang="de">
<head>
<meta charset="utf-8">
<title>Klangwerk Aurel – Visitenkarte</title>
<link rel="stylesheet" href="https://fonts.googleapis.com/css2?family=Montserrat:wght@400;500;800&display=swap">
<style>
  :root{
    --bg:#8a8a8a;
    --card:#2b2b2b;
    --orange:#ef6a1f;
    --white:#f2f2f2;
    --divider:#6e6e6e;
  }
  *{box-sizing:border-box;margin:0;padding:0}
  html,body{width:1200px;height:1021px;overflow:hidden}
  body{
    background:var(--bg);
    font-family:"Montserrat",sans-serif;
    position:relative;
  }
  .card{
    position:absolute;
    left:280px;
    width:640px;
    height:366px;
    background:var(--card);
    box-shadow:0 10px 30px rgba(0,0,0,.35);
  }
  .card--front{top:100px}
  .card--back{top:540px}

  .brand{
    position:absolute;
    left:0;right:0;
    text-align:center;
    color:var(--orange);
    font-weight:800;
    font-size:46px;
    letter-spacing:1px;
    text-transform:uppercase;
  }
  .card--front .brand{top:140px}
  .card--back .brand{top:58px}

  .front-url{
    position:absolute;
    left:0;right:0;bottom:48px;
    text-align:center;
    color:var(--white);
    font-size:14px;
    font-weight:500;
    letter-spacing:6px;
  }
  .front-url .accent{color:var(--orange)}

  .person{
    position:absolute;
    right:350px;
    top:178px;
    text-align:right;
  }
  .person__name{
    color:var(--orange);
    font-weight:800;
    font-size:22px;
  }
  .person__role{
    color:var(--white);
    font-size:15px;
    margin-top:4px;
  }
  .divider{
    position:absolute;
    left:306px;
    top:172px;
    width:2px;
    height:80px;
    background:var(--divider);
  }
  .contact{
    position:absolute;
    left:330px;
    top:182px;
    list-style:none;
    color:var(--white);
    font-size:17px;
    font-weight:500;
    line-height:27px;
  }
  .contact li{display:flex;align-items:center;gap:9px}
  .contact svg{width:15px;height:15px;flex:none}
  .address{
    position:absolute;
    left:0;right:0;
    top:290px;
    text-align:center;
    color:var(--white);
    font-size:17px;
    font-weight:500;
  }
</style>
</head>
<body>

<section class="card card--front">
  <div class="brand">Klangwerk Aurel</div>
  <p class="front-url">www.<span class="accent">klangwerk</span>.ch</p>
</section>

<section class="card card--back">
  <div class="brand">Klangwerk Aurel</div>

  <div class="person">
    <p class="person__name">Lukas Brenner</p>
    <p class="person__role">Owner</p>
  </div>

  <div class="divider"></div>

  <ul class="contact">
    <li>
      <svg viewBox="0 0 16 16" aria-hidden="true"><path fill="#ef6a1f" d="M3.6 1.2l2.3 2.6-1.3 1.8c.9 2 2.4 3.6 4.4 4.6l1.8-1.3 2.6 2.3-1.4 2.3C7 13.5 2.6 9 2.4 3z"/></svg>
      041 555 01 72
    </li>
    <li>
      <svg viewBox="0 0 16 16" aria-hidden="true"><rect x="1" y="3" width="14" height="10" fill="none" stroke="#ef6a1f" stroke-width="1.6"/><path d="M1 3l7 6 7-6" fill="none" stroke="#ef6a1f" stroke-width="1.6"/></svg>
      info@klangwerk.ch
    </li>
    <li>
      <svg viewBox="0 0 16 16" aria-hidden="true"><g fill="none" stroke="#ef6a1f" stroke-width="1.3"><circle cx="8" cy="8" r="6.5"/><ellipse cx="8" cy="8" rx="3" ry="6.5"/><path d="M1.5 8h13M2.5 4.8h11M2.5 11.2h11"/></g></svg>
      www.klangwerk.ch
    </li>
  </ul>

  <p class="address">Mühlegasse 18, CH-6004 Luzern</p>
</section>

</body>
</html>
```